Varnek Group Business Card

Varnek Group — Business Card Design Brief
Overview
Design a double-sided business card for Varnek Group that highlights our two service arms: Varnek Communications (telecommunications) and Varnek Energy (business energy solutions). The card should feel smart and stand out when handed to clients.

Objectives
Showcase our areas of specialty clearly.
Reflect the overall Varnek / Varnek Group brand while acknowledging both arms.
Explore using both logos (Communications + Energy) or one unified logo, depending on the design.

Deliverables
One double-sided business card design (front + back).

Content & Copy
Front (preferred): Logo: Varnek / Varnek Group
Descriptor: Business Communications | Business Energy
Back:My contact details and company details
Core products: Business Mobile • Telephony • Internet • Business Energy Solutions

Brand & Visual Direction
We have a group logo currently tailored more toward telecoms, plus a separate Varnek Energy logo.
Please explore layouts that use both logos or just one, whichever works best.
Color: I wouldn't mind seeing an option using our the Blue/Purple gradient from our website (varnek-example.co.uk), but also open to non-gradient approaches and other colours..

Overall look: Smart, modern, and distinctive.
Format & Print Specs
Double-sided business card format. (Use a standard size

Must-Haves
Front: Varnek wording or Varnek Group wording with atleast 1 logo also on front “Business Communications | Business Energy.”

Back: Contact + company details and core products.
A design that stands out while remaining professional.

Nice-to-Have Options
A gradient version using our site’s Blue/Purple gradient.
A non-gradient version.
A dual-logo treatment versus a single-logo treatment.

Thanks
Dominic

```html
<!DOCTYPE html>
<html lang="en">
<head>
<meta charset="utf-8">
<title>Varnek Group Business Card</title>
<link href="https://fonts.googleapis.com/css2?family=Poppins:wght@400;500;600;700&display=swap" rel="stylesheet">
<style>
  :root {
    --page: #d9d4cc;
    --card-top: #f4f6f8;
    --card-bottom: #e4e9ee;
    --navy: #1f3d7c;
    --ink: #23304a;
    --deep: #141b3c;
    --teal: #1c6f93;
    --band-start: #26346f;
    --band-end: #157394;
    --band-text: #bccde2;
    --mark: #1d62c8;
  }
  * { box-sizing: border-box; margin: 0; padding: 0; }
  html, body { width: 1200px; height: 970px; overflow: hidden; }
  body {
    background: var(--page);
    font-family: "Poppins", sans-serif;
    position: relative;
  }
  .card {
    position: absolute;
    left: 100px; top: 199px;
    width: 1000px; height: 572px;
    border-radius: 26px;
    overflow: hidden;
    background: linear-gradient(160deg, var(--card-top), var(--card-bottom));
    box-shadow: 0 18px 40px rgba(40, 35, 30, 0.22);
  }
  .accent-bar {
    position: absolute;
    left: 0; top: 112px;
    width: 25px; height: 56px;
    background: linear-gradient(180deg, var(--teal), var(--navy));
  }
  .holder-name {
    position: absolute;
    left: 68px; top: 108px;
    font-size: 34px; font-weight: 600;
    color: var(--navy);
    letter-spacing: 0.3px;
  }
  .holder-title {
    position: absolute;
    left: 67px; top: 152px;
    font-size: 21px; font-weight: 400;
    color: var(--ink);
    letter-spacing: 1.2px;
  }
  .address {
    position: absolute;
    left: 67px; top: 262px;
    font-size: 24px; line-height: 30px;
    color: var(--ink);
  }
  .contacts {
    position: absolute;
    left: 70px; top: 362px;
    list-style: none;
  }
  .contacts li {
    display: flex; align-items: center;
    height: 34px;
    font-size: 24px;
    color: var(--ink);
  }
  .contacts svg { width: 27px; height: 27px; margin-right: 17px; flex: none; }
  .brand {
    position: absolute;
    left: 640px; top: 50px;
    width: 290px;
    display: flex; flex-direction: column; align-items: center;
  }
  .brand-dot {
    width: 120px; height: 120px;
    border-radius: 50%;
    background: var(--mark);
  }
  .brand-name {
    margin-top: 22px;
    font-size: 62px; font-weight: 700;
    color: var(--deep);
    letter-spacing: 1px;
    line-height: 1;
  }
  .services {
    position: absolute;
    left: 0; top: 485px;
    width: 100%; height: 55px;
    background: linear-gradient(90deg, var(--band-start), var(--band-end));
    display: flex; align-items: center;
    padding-left: 59px;
    font-size: 26px;
    color: var(--band-text);
    letter-spacing: 0.4px;
  }
</style>
</head>
<body>
  <main class="card">
    <div class="accent-bar"></div>
    <h1 class="holder-name">ELLIOT R HALE</h1>
    <p class="holder-title">BUSINESS DEVELOPMENT MANAGER</p>

    <address class="address">4100 Harbor Lane ste 210<br>Brookton WA 12345</address>

    <ul class="contacts">
      <li>
        <svg viewBox="0 0 24 24" aria-hidden="true"><circle cx="12" cy="12" r="12" fill="#1c6f93"/><path d="M8.5 6.5c.5-.4 1.2-.3 1.5.2l1 1.8c.3.5.1 1.1-.3 1.4l-.7.5c.5 1.4 1.6 2.6 3 3.2l.5-.7c.3-.4 1-.6 1.4-.3l1.8 1c.5.3.6 1 .2 1.5l-.8.9c-.6.6-1.5.8-2.3.5-3-1.2-5.3-3.5-6.4-6.5-.3-.8-.1-1.7.5-2.3z" fill="#fff"/></svg>
        (456) 555-0142
      </li>
      <li>
        <svg viewBox="0 0 24 24" aria-hidden="true"><circle cx="12" cy="12" r="12" fill="#1c6f93"/><rect x="6" y="8" width="12" height="8.5" rx="1" fill="none" stroke="#fff" stroke-width="1.4"/><path d="M6.5 8.5l5.5 4.3 5.5-4.3" fill="none" stroke="#fff" stroke-width="1.4"/></svg>
        elliot@varnekmail.example
      </li>
      <li>
        <svg viewBox="0 0 24 24" aria-hidden="true"><circle cx="12" cy="12" r="12" fill="#1c6f93"/><g fill="none" stroke="#fff" stroke-width="1.2"><circle cx="12" cy="12" r="6"/><ellipse cx="12" cy="12" rx="2.6" ry="6"/><path d="M6 12h12M7 9h10M7 15h10"/></g></svg>
        www.varnek-example.co.uk
      </li>
    </ul>

    <div class="brand">
      <div class="brand-dot"></div>
      <div class="brand-name">VARNEK</div>
    </div>

    <p class="services">Business Mobile • Telephony • Internet • Business Energy Solutions</p>
  </main>
</body>
</html>
```